Bluefern Slimming Clinic

build a landing page website using the content from this websites. we want to copy all the content from harrowvalecourses.com but make page look more professional. we dont have a logo yet but url is www.bluefernslimmingclinic.com
https://quillbanktrimalliance.com/home-page
https://www.harrowvalecourses.com/

Target Market(s)

people looking to open a weightloss clinic or a franchise opportunity

Coding

Coded - Design and coding required

Number of Pages Required

3 page

Requirements
Must have
• copy all content from other site https://www.harrowvalecourses.com/

```html
<!DOCTYPE html>
<html lang="en">
<head>
<meta charset="utf-8">
<title>Bluefern Slimming Clinic – Start Your Own Weight Loss Clinic</title>
<link href="https://fonts.googleapis.com/css2?family=Poppins:wght@400;500;600;700;800&family=Roboto:wght@400;500&display=swap" rel="stylesheet">
<style>
:root{
  --yellow:#f6b21b;
  --yellow-soft:#f8c957;
  --ink:#111111;
  --text:#222222;
  --grey-bg:#f2f2f2;
  --dark:#2b2b2b;
  --darker:#262626;
  --field:#e1e1e1;
  --white:#ffffff;
}
*{margin:0;padding:0;box-sizing:border-box}
html,body{width:1200px;height:3361px;overflow:hidden}
body{position:relative;background:var(--white);font-family:"Roboto",Arial,sans-serif;color:var(--text)}
.abs{position:absolute}
.heading{font-family:"Poppins",Arial,sans-serif;font-weight:700;color:var(--ink)}
.accent{color:var(--yellow)}
.btn{position:absolute;display:flex;align-items:center;justify-content:center;font-family:"Roboto",Arial,sans-serif;font-size:14px;border-radius:6px}
.btn-solid{background:var(--yellow);color:var(--white)}
.btn-outline{border:2px solid var(--yellow);color:var(--ink);background:var(--white);font-size:15px}

/* header */
.brand{position:absolute;top:20px;left:100px;display:flex;align-items:center;gap:8px;font-family:"Poppins",sans-serif;font-weight:600;font-size:14px;color:var(--white)}
.brand-dot{width:14px;height:14px;border-radius:50%;background:var(--white)}
.nav{position:absolute;top:21px;left:469px;display:flex;gap:0;font-family:"Roboto",sans-serif;font-size:15px;color:var(--ink)}
.nav a{color:var(--ink);text-decoration:none;position:absolute;white-space:nowrap}
.search{position:absolute;left:983px;top:13px;width:114px;height:30px;border:2px solid var(--white);border-radius:6px;color:var(--white);font-size:15px;padding:4px 0 0 15px}
.search svg{position:absolute;right:12px;top:6px}

/* hero */
.hero-title{left:565px;top:120px;font-size:41px;line-height:49px}
.hero-copy{left:565px;top:238px;width:540px;font-size:15px;line-height:18.5px;color:var(--ink)}
.hero-copy p{margin-bottom:11px}

/* welcome */
.welcome{left:0;top:541px;width:1200px;height:566px;background:var(--grey-bg)}
.welcome-kicker{left:100px;top:628px;font-size:33px;font-weight:600;color:var(--yellow)}
.welcome-title{left:100px;top:664px;font-size:41px;font-weight:800}
.welcome-sub{left:100px;top:713px;font-family:"Poppins",sans-serif;font-weight:600;font-size:23px;color:var(--ink)}
.welcome-copy{left:100px;top:755px;width:600px;font-family:"Poppins",sans-serif;font-size:13.5px;line-height:20px;color:var(--ink)}
.welcome-copy p{margin-bottom:20px}

/* offer */
.section-title{width:1200px;left:0;text-align:center;font-size:41px}
.section-sub{width:1200px;left:0;text-align:center;font-size:15px;color:var(--ink)}
.offer-item{position:absolute;top:1220px;width:200px;text-align:center;font-size:15px;line-height:18.5px;color:var(--ink)}
.offer-icon{width:56px;height:56px;margin:0 auto 20px;border-radius:12px;background:linear-gradient(135deg,#fde3a6,#f6b21b)}

/* compare / get started */
.compare-photo{left:0;top:1433px;width:600px;height:284px;background:linear-gradient(120deg,#5a5e5a 0%,#3b3e39 40%,#4f6b3a 75%,#8a5a2b 100%)}
.compare-shade{left:0;top:1433px;width:600px;height:284px;background:rgba(20,20,20,.45)}
.compare-title{left:100px;top:1474px;font-size:40px;font-weight:800;color:var(--white)}
.compare-list{font-size:14.5px;line-height:18.5px;color:var(--white);list-style:none}
.started{left:600px;top:1433px;width:600px;height:284px;background:var(--dark)}
.started-kicker{left:600px;top:1458px;width:506px;text-align:center;font-size:20px;color:var(--white)}
.started-title{left:600px;top:1480px;width:506px;text-align:center;font-size:39px;font-weight:800;color:var(--yellow)}
.step{position:absolute;top:1533px;width:160px;text-align:center}
.step-num{width:24px;height:24px;margin:0 auto;border-radius:50%;background:var(--yellow);color:var(--dark);font-family:"Poppins",sans-serif;font-weight:700;font-size:14px;line-height:24px}
.step-name{margin-top:10px;font-size:16px;color:var(--yellow);line-height:18px}
.step-copy{margin-top:14px;font-size:11.5px;line-height:14px;color:var(--white)}

/* testimonials */
.card{position:absolute;width:417px;height:166px;background:var(--white);box-shadow:0 3px 6px rgba(0,0,0,.18)}
.card-side{position:absolute;left:0;top:0;width:166px;height:166px;background:var(--yellow-soft)}
.card-avatar{position:absolute;left:36px;top:21px;width:95px;height:124px;border-radius:48px;background:linear-gradient(180deg,#f3f0ec,#d9d3cc)}
.card-text{position:absolute;left:180px;top:38px;width:222px;text-align:center;font-size:13px;line-height:16px;color:var(--ink)}
.card-name{margin-top:14px;font-weight:500}

/* partners */
.partners{left:0;top:2344px;width:1200px;height:178px;background:var(--darker)}

/* contact */
.contact-title{left:630px;top:2592px;font-size:40px;line-height:48px}
.field{position:absolute;height:32px;background:var(--field);border-radius:6px;font-size:13.5px;color:var(--ink);padding:9px 0 0 10px}

/* footer */
.footer{left:0;top:3017px;width:1200px;height:344px;background:var(--dark)}
.footer-brand{left:100px;top:3072px;display:flex;align-items:center;gap:8px;font-family:"Poppins",sans-serif;font-weight:600;font-size:14px;color:var(--white)}
.footer-copy{left:100px;top:3108px;width:390px;font-family:"Poppins",sans-serif;font-size:15px;line-height:22px;color:var(--white)}
.footer-col{position:absolute;top:3108px;color:var(--white)}
.footer-col h4{font-family:"Roboto",sans-serif;font-weight:400;font-size:17px;margin-bottom:14px}
.footer-col li{list-style:none;font-family:"Poppins",sans-serif;font-size:14.5px;line-height:31px}
.footer-rule{left:58px;top:3310px;width:1100px;height:2px;background:var(--white)}
.legal{top:3327px;font-family:"Poppins",sans-serif;font-size:13px;color:var(--white)}
</style>
</head>
<body>

<!-- header & hero -->
<svg class="abs" style="left:0;top:0" width="1200" height="541" viewBox="0 0 1200 541">
  <path d="M0 0 H370 C250 40 150 120 150 270 C150 420 280 500 460 500 C500 505 530 520 545 541 H0 Z" fill="var(--yellow)"/>
  <path d="M722 0 H1100 C1095 30 1050 47 960 48 C850 50 760 40 722 0 Z" fill="var(--yellow)"/>
  <circle cx="342" cy="21" r="6" fill="var(--yellow-soft)"/>
  <circle cx="1157" cy="99" r="15" fill="var(--yellow-soft)"/>
  <circle cx="844" cy="468" r="15" fill="var(--yellow-soft)"/>
  <path d="M220 170 C150 230 160 400 260 450 C330 485 420 460 455 400" fill="none" stroke="var(--yellow)" stroke-width="6"/>
  <defs><linearGradient id="heroPhoto" x1="0" y1="0" x2="0" y2="1"><stop offset="0" stop-color="#f1e4d6"/><stop offset=".55" stop-color="#c9283a"/><stop offset="1" stop-color="#e6c2a4"/></linearGradient></defs>
  <path role="img" aria-label="Photo of a smiling woman in red sportswear holding bell peppers and a tape measure" d="M210 180 C230 80 330 55 400 110 C470 170 470 330 430 410 C390 470 270 470 225 400 C190 340 195 250 210 180 Z" fill="url(#heroPhoto)"/>
</svg>

<div class="brand"><span class="brand-dot"></span>Bluefern Slimming Clinic</div>
<nav class="nav">
  <a style="left:0">Home</a>
  <a style="left:63px">About Us</a>
  <a style="left:157px">What We Offer</a>
  <a style="left:298px">Compare</a>
  <a style="left:389px">FAQ</a>
  <a style="left:435px">Contact</a>
</nav>
<div class="search">Search
  <svg width="14" height="14" viewBox="0 0 14 14"><circle cx="6" cy="6" r="4.5" fill="none" stroke="#fff" stroke-width="2"/><path d="M9.5 9.5 13 13" stroke="#fff" stroke-width="2"/></svg>
</div>

<h1 class="abs heading hero-title"><span class="accent">Start Your</span> Own Profitable<br>Weight <span class="accent">Loss Clinic!</span></h1>
<div class="abs hero-copy">
  <p>We are not a weight loss franchise – you are simply buying our business model, training and support for one low fee. Please read about us, look at what we offer and compare us to&nbsp; weight loss franchises the marketplace.</p>
  <p>We offer a free market analysis and sample break even analysis your area.</p>
  <p>We think you will be happy you found us!</p>
</div>
<a class="btn btn-outline" style="left:565px;top:367px;width:116px;height:33px">Learn More</a>

<!-- welcome -->
<div class="abs welcome"></div>
<div class="abs heading welcome-kicker">Welcome There</div>
<h2 class="abs heading welcome-title">Start Your Own</h2>
<div class="abs welcome-sub">Weight Loss &amp; Wellness Center</div>
<div class="abs welcome-copy">
  <p>Bluefern Slimming Clinic Now Offers Our Model To You So You Can Add Weight Loss And Wellness Programs To Your Existing Medical Practice Or Open A Stand Alone Weight Loss And Wellness Center.</p>
  <p>We Are Not A Weight Loss Franchise – You Are Simply Buying Our Business Model, Training And Support For One Low Fee. Please Read About Us, Look At What We Offer And Compare Us To Weight Loss Franchises In The Marketplace.</p>
  <p>We Now Offer You A Free Market Analysis And Sample Break Even Analysis For Your Area. Please See Our Contact Page.</p>
  <p>We Think You Will Be Happy You Found Us !</p>
</div>
<a class="btn btn-solid" style="left:100px;top:1007px;width:116px;height:32px">INFO MORE</a>
<svg class="abs" style="left:730px;top:625px" width="400" height="410" viewBox="0 0 400 410">
  <defs><linearGradient id="clinicPhoto" x1="0" y1="0" x2="1" y2="1"><stop offset="0" stop-color="#dfe5ea"/><stop offset=".5" stop-color="#6b7480"/><stop offset="1" stop-color="#2d333a"/></linearGradient></defs>
  <path d="M20 175 C20 80 130 10 230 10 C330 10 390 80 388 170 C385 280 320 400 220 405 C160 408 130 340 90 300 C50 265 20 240 20 175 Z" fill="none" stroke="var(--yellow)" stroke-width="5"/>
  <path role="img" aria-label="Photo of a patient on an exercise machine during a clinical fitness test" d="M55 150 C80 60 170 20 260 25 C340 30 400 100 395 180 C390 270 340 360 280 380 C210 400 150 330 110 290 C70 250 45 210 55 150 Z" fill="url(#clinicPhoto)"/>
</svg>

<!-- what we offer -->
<h2 class="abs heading section-title" style="top:1122px">What <span class="accent">We Offer</span></h2>
<div class="abs section-sub" style="top:1171px">It Is A Long Established Fact That A Reader Will Be Distracted By The Readable Content</div>
<div class="offer-item" style="left:129px"><div class="offer-icon" role="img" aria-label="Icon of a trainer teaching a student"></div>One-On-One<br>Business &amp;<br>Medical Training</div>
<div class="offer-item" style="left:392px"><div class="offer-icon" role="img" aria-label="Icon of marketing channels"></div>Marketing &amp;<br>Advertising<br>Training</div>
<div class="offer-item" style="left:645px"><div class="offer-icon" role="img" aria-label="Icon of a healthy diet plate"></div>Diets, Patient<br>Protocols &amp;<br>Programs</div>
<div class="offer-item" style="left:893px"><div class="offer-icon" role="img" aria-label="Icon of a person at an office desk"></div>Office &amp;<br>Operations<br>Manuals</div>

<!-- compare & get started -->
<div class="abs compare-photo" role="img" aria-label="Photo of a weight loss chart, stethoscope and fresh salad"></div>
<div class="abs compare-shade"></div>
<h2 class="abs heading compare-title">COMPARE</h2>
<ul class="abs compare-list" style="left:100px;top:1546px">
  <li>&gt; No Franchise Fees</li><li>&gt; No Scope Of Practice Limits</li><li>&gt; No Territory Fees</li><li>&gt; No Convention Fees</li>
</ul>
<ul class="abs compare-list" style="left:349px;top:1546px">
  <li>&gt; No Monthly Licensing Fees</li><li>&gt; No % Royalties</li><li>&gt; No % Advertising Fees</li><li>&gt; No Mandatory Vendors</li>
</ul>
<a class="btn btn-solid" style="left:100px;top:1643px;width:117px;height:30px;font-size:13.5px">Compare Now</a>

<div class="abs started"></div>
<div class="abs started-kicker" style="left:600px;width:506px">It’s Easy</div>
<h2 class="abs heading started-title">GET STARTED TODAY</h2>
<div class="step" style="left:614px"><div class="step-num">1</div><div class="step-name">Contact Us</div><div class="step-copy">Contact Us For More<br>Information On Our<br>Model</div></div>
<div class="step" style="left:777px"><div class="step-num">2</div><div class="step-name">Visit Us</div><div class="step-copy">Schedule A Time To Visit<br>Atlanta And See Our<br>Clinics In Action</div></div>
<div class="step" style="left:950px"><div class="step-num">3</div><div class="step-name">Schedule a<br>Webinar</div><div class="step-copy" style="margin-top:16px">Schedule Your One-On-<br>One 20 Minute Webinar</div></div>
<a class="btn btn-solid" style="left:748px;top:1658px;width:211px;height:32px;font-size:13.5px">CONTACT US GET STARTED</a>

<!-- testimonials -->
<h2 class="abs heading section-title accent" style="top:1797px">Testimonial</h2>
<div class="abs section-sub" style="top:1851px">It Is A Long Established Fact That A Reader Will Be Distracted</div>
<div class="card" style="left:100px;top:1894px"><div class="card-side"><div class="card-avatar" role="img" aria-label="Portrait photo of a client"></div></div><div class="card-text">It Is A Long Established Fact That A Reader Will Be Distracted By The Readable Content Of A Page When Looking At Its Layout.<div class="card-name">Mara Lindqvist</div></div></div>
<div class="card" style="left:683px;top:1894px"><div class="card-side"><div class="card-avatar" role="img" aria-label="Portrait photo of a client"></div></div><div class="card-text">It Is A Long Established Fact That A Reader Will Be Distracted By The Readable Content Of A Page When Looking At Its Layout.<div class="card-name">Tomas Brell</div></div></div>
<div class="card" style="left:392px;top:2094px"><div class="card-side"><div class="card-avatar" role="img" aria-label="Portrait photo of a client"></div></div><div class="card-text">It Is A Long Established Fact That A Reader Will Be Distracted By The Readable Content Of A Page When Looking At Its Layout.<div class="card-name">OWEN PARDO</div></div></div>

<!-- partners -->
<div class="abs partners"></div>
<svg class="abs" style="left:0;top:2344px" width="1200" height="178" viewBox="0 0 1200 178">
  <circle role="img" aria-label="Accreditation badge" cx="222" cy="90" r="62" fill="#1d6fa5"/>
  <rect role="img" aria-label="Professional society badge" x="395" y="22" width="340" height="134" rx="10" fill="#4b4b4b"/>
  <rect role="img" aria-label="Medical academy badge" x="845" y="22" width="200" height="134" rx="8" fill="#2f5f9e"/>
</svg>

<!-- contact -->
<svg class="abs" style="left:150px;top:2570px" width="420" height="410" viewBox="0 0 420 410">
  <defs><linearGradient id="dietPhoto" x1="0" y1="0" x2="1" y2="1"><stop offset="0" stop-color="#e9e4dc"/><stop offset=".6" stop-color="#b9a58a"/><stop offset="1" stop-color="#6e5a3e"/></linearGradient></defs>
  <path d="M70 80 C120 20 210 0 260 40 C300 75 300 160 360 200 C420 240 410 320 350 360 C280 405 150 410 80 350 C10 290 10 150 70 80 Z" fill="var(--yellow)"/>
  <path role="img" aria-label="Photo of hands holding a diet plan and a tablet" d="M88 92 C135 40 210 25 250 60 C285 92 282 170 340 210 C390 245 380 315 330 345 C265 385 155 390 95 335 C35 280 38 150 88 92 Z" fill="url(#dietPhoto)"/>
</svg>
<h2 class="abs heading contact-title"><span class="accent">Contact Us</span><br>Today to Learn More</h2>
<div class="field" style="left:630px;top:2708px;width:224px">Full Name</div>
<div class="field" style="left:875px;top:2708px;width:225px">Email</div>
<div class="field" style="left:630px;top:2758px;width:224px">Phone</div>
<div class="field" style="left:875px;top:2758px;width:225px">City/State</div>
<div class="field" style="left:630px;top:2806px;width:470px;height:66px">Message</div>
<a class="btn btn-solid" style="left:630px;top:2892px;width:116px;height:30px;font-size:13.5px">SUBMIT INFO</a>

<!-- footer -->
<div class="abs footer"></div>
<div class="abs footer-brand"><span class="brand-dot"></span>Bluefern Slimming Clinic</div>
<div class="abs footer-copy">It Is A Long Established Fact That A Reader Will Be Distracted By The Readable Content Of A Page When Looking At Its Layout. The Point Of Using Lorem Ipsum .<br><br>@2019 Harrowvale Courses Ltd</div>
<div class="footer-col" style="left:556px"><h4>ABOUT</h4><ul><li>FAQ</li><li>Career</li><li>About Us</li><li>Resources</li></ul></div>
<div class="footer-col" style="left:753px"><h4>SERVICES</h4><ul><li>Support Portal</li><li>Wellness Club</li><li>For Employers</li><li>Services</li></ul></div>
<div class="footer-col" style="left:950px"><h4>CONTACT US</h4><ul><li>877-555-0143</li><li style="line-height:22px;margin-top:5px">info@harrowvale<br>courses.com</li></ul></div>
<div class="abs footer-rule"></div>
<div class="abs legal" style="left:100px">Copyright © 2021 NORTHGATE LOCAL All Rights Reserved.</div>
<div class="abs legal" style="left:870px">Terms &amp;Conditions,Privacy / Sitemap</div>

</body>
</html>
```